Electrician Needs A Business Card

I already have a logo and would like a business card to be designed based around this logo the company is called Tolvane Electrical Pty Ltd

The business card will be printed on transparent plastic so I need it to stand out from the crowd. I do not want the card to have anything to do with Electrical on it eg light bulbs, power points etc

I need it to have the following details.

Gareth Pomfrey
Mobile : 0437 519 284
email : gareth@tolvaneelectrical.com.au

If it could incorporate the following onto the bottom of the card
ELECTRICAL - COMMUNICATIONS - AUDIO - VISUAL

```html
<!DOCTYPE html>
<html lang="en">
<head>
<meta charset="utf-8">
<title>Tolvane Electrical – Business Card</title>
<link href="https://fonts.googleapis.com/css2?family=Noto+Sans:ital,wght@0,400;0,500;1,400&display=swap" rel="stylesheet">
<style>
  :root {
    --backdrop: #b7a584;
    --card: #e8e3da;
    --ink: #141414;
    --accent: #f5a623;
    --accent-soft: #f2cf8f;
    --pattern-grey: #a8a29a;
    --tagline: #a77826;
  }
  * { margin: 0; padding: 0; box-sizing: border-box; }
  html, body {
    width: 1200px;
    height: 1000px;
    overflow: hidden;
    background: var(--backdrop);
    font-family: "Noto Sans", sans-serif;
  }
  .card {
    position: absolute;
    left: 152px;
    top: 245px;
    width: 896px;
    height: 552px;
    background: var(--card);
  }
  .pattern-band {
    position: absolute;
    left: 13px;
    top: 25px;
    width: 870px;
    height: 130px;
    background: linear-gradient(180deg, var(--pattern-grey) 0%, var(--accent-soft) 40%, var(--accent-soft) 60%, var(--pattern-grey) 100%);
    opacity: 0.75;
  }
  .brand {
    position: absolute;
    left: 73px;
    top: 258px;
    display: flex;
    align-items: center;
    gap: 22px;
  }
  .brand-square {
    width: 110px;
    height: 110px;
    background: var(--accent);
  }
  .brand-name {
    font-size: 40px;
    font-weight: 400;
    line-height: 1.05;
    color: var(--ink);
  }
  .divider {
    position: absolute;
    left: 446px;
    top: 248px;
    width: 3px;
    height: 147px;
    background: var(--accent);
  }
  .contact {
    position: absolute;
    left: 481px;
    top: 268px;
    color: var(--ink);
  }
  .contact-name {
    font-size: 26px;
    font-weight: 400;
    margin-bottom: 26px;
  }
  .contact-line {
    display: flex;
    align-items: center;
    gap: 10px;
    font-size: 18px;
    line-height: 27px;
  }
  .contact-line svg { width: 28px; height: 20px; flex: none; }
  .services {
    position: absolute;
    left: 0;
    right: 0;
    top: 484px;
    text-align: center;
    font-size: 26px;
    font-style: italic;
    letter-spacing: 1px;
    color: var(--tagline);
  }
</style>
</head>
<body>
  <div class="card">
    <div class="pattern-band" role="img" aria-label="Repeating band of faceted cube shapes in grey and soft orange"></div>

    <div class="brand">
      <div class="brand-square"></div>
      <div class="brand-name">Tolvane<br>Electrical</div>
    </div>

    <div class="divider"></div>

    <div class="contact">
      <p class="contact-name">Gareth Pomfrey</p>
      <p class="contact-line">
        <svg viewBox="0 0 28 20" aria-hidden="true">
          <path d="M2 7 Q14 -1 26 7 L23 10 L19 8 L19 5 Q14 3 9 5 L9 8 L5 10 Z" fill="#f5a623"/>
          <path d="M6 11 L10 8 L18 8 L22 11 L22 19 L6 19 Z" fill="#f5a623"/>
          <circle cx="14" cy="14" r="2.5" fill="#e8e3da"/>
        </svg>
        0437 519 284
      </p>
      <p class="contact-line">
        <svg viewBox="0 0 28 20" aria-hidden="true">
          <rect x="2" y="3" width="24" height="15" fill="#f5a623"/>
          <path d="M2 3 L14 12 L26 3" fill="none" stroke="#e8e3da" stroke-width="1.8"/>
          <path d="M2 18 L11 10 M26 18 L17 10" stroke="#e8e3da" stroke-width="1.5"/>
        </svg>
        gareth@tolvaneelectrical.com.au
      </p>
    </div>

    <p class="services">ELECTRICAL - COMMUNICATIONS - AUDIO - VISUAL</p>
  </div>
</body>
</html>
```